Author Website Design

The purpose of the site will be to promote "Harbor," an edgy new thriller from Marcus Pellerin. I'd like the site to correspond with the design and colors of the book's cover, as I'm focused on creating a recognizable brand. Designers are of course encouraged to put their own artistic stamp on the project, but its important to integrate the site's design with the cover.

Requirements
Must have
• Site must be integrated with/correspond to the design of my book cover. The site should have the following pages: About; Books; Velm Quarter; Contact; Blog.

The site should link readers to the various retailers where Harbor is available

```html
<!DOCTYPE html>
<html lang="en">
<head>
<meta charset="utf-8">
<title>Harbor — Marcus Pellerin</title>
<link rel="stylesheet" href="https://fonts.googleapis.com/css2?family=Archivo+Black&family=Russo+One&family=Oswald:wght@400;500&family=Noto+Serif&family=Arvo:wght@700&family=Alfa+Slab+One&display=swap">
<style>
:root{
  --ink:#000;
  --panel:#0b0906;
  --gold:#ffc400;
  --orange:#f08a10;
  --rust:#c2410c;
  --red:#d7301a;
  --muted:#5a4a2c;
  --text-yellow:#ffe800;
  --white:#fff;
}
*{box-sizing:border-box;margin:0;padding:0}
html,body{width:1188px;height:1200px;overflow:hidden;background:var(--ink)}
body{position:relative;font-family:Arial,Helvetica,sans-serif}
a{text-decoration:none;color:inherit}

.main-nav{position:absolute;left:26px;top:4px;width:1136px;height:58px;
  background:linear-gradient(180deg,#ffe44a 0%,var(--gold) 55%,#f5a300 100%);
  display:flex;justify-content:space-between;align-items:center;padding:0 40px}
.main-nav a{font-family:"Archivo Black",sans-serif;font-size:30px;color:#111;letter-spacing:.3px}

.intro-panel{position:absolute;left:26px;top:66px;width:564px;height:556px;
  background:linear-gradient(180deg,#141109 0%,var(--panel) 40%,#060504 100%);
  border:8px solid #1c1912;box-shadow:inset 0 0 30px #000}
.intro-title{position:absolute;left:24px;top:36px;font-family:"Russo One",sans-serif;font-size:38px;
  color:var(--orange);letter-spacing:1px}
.intro-copy{position:absolute;left:24px;top:86px;width:478px;font-size:16.2px;line-height:21px;color:var(--text-yellow)}
.intro-copy p+p{margin-top:21px}
.intro-signature{position:absolute;left:24px;top:458px;font-family:"Oswald",sans-serif;font-weight:500;
  font-size:40px;color:#4a3510;letter-spacing:.5px}

.cover-art{position:absolute;left:590px;top:66px;width:576px;height:588px;
  background:radial-gradient(ellipse at 60% 55%,#8a6a3a 0%,#3b3530 35%,#1c1f26 60%,#050505 100%)}

.author-words{position:absolute;left:28px;top:668px;width:790px}
.section-title{font-family:"Noto Serif",serif;font-size:27px;color:var(--orange);font-weight:400;line-height:37px}
.author-words .section-title{padding-bottom:10px;border-bottom:1px dashed #3a3a3a}
.review{margin-top:18px;font-size:16.2px;line-height:21px;color:var(--text-yellow)}
.review p+p{margin-top:21px}
.review-source{margin-top:14px;padding-top:12px;border-top:1px dashed #3a3a3a;
  font-family:"Noto Serif",serif;font-size:19px;color:var(--muted)}
.review-source em{font-style:normal;color:var(--gold)}

.retailers{position:absolute;left:832px;top:676px;width:330px}
.retail-list{list-style:none;margin:16px 0 0 52px}
.retail-list li{font-size:16px;line-height:28px;color:var(--orange)}
.retail-list li::before{content:"»";font-size:12px;margin-right:10px;color:var(--orange)}
.retail-list li:nth-child(n+2){color:#5e4a30}
.retail-list li:nth-child(n+2)::before{color:#6a4a20}
.more-shops{position:absolute;left:1036px;top:930px;font-size:16px;color:var(--orange)}
.more-shops::before{content:"";display:inline-block;border-left:8px solid var(--orange);
  border-top:6px solid transparent;border-bottom:6px solid transparent;margin-right:10px}

.promo{position:absolute;top:966px;height:120px;border:2px solid #3a1a05;overflow:hidden}
.promo-buy{left:26px;width:372px;background:linear-gradient(180deg,var(--gold) 0%,var(--orange) 55%,var(--red) 100%)}
.promo-free{left:410px;width:371px;background:linear-gradient(90deg,var(--rust) 0%,var(--orange) 50%,var(--gold) 100%)}
.promo-signup{left:793px;width:373px;background:linear-gradient(180deg,var(--gold) 0%,var(--orange) 55%,var(--red) 100%)}
.buy-label{position:absolute;left:8px;top:26px;font-family:"Alfa Slab One",serif;color:#3a1606;font-size:30px;line-height:30px}
.buy-label small{display:block;font-family:Arial,sans-serif;font-size:15px;font-weight:bold;line-height:20px}
.book-thumb{position:absolute;left:268px;top:6px;width:96px;height:106px;
  background:linear-gradient(160deg,#2a2a2a,#6b5a3a 60%,#111)}
.price-tag{position:absolute;left:312px;top:80px;transform:rotate(-45deg);font-size:14px;color:#111;font-weight:bold}
.free-label{position:absolute;left:8px;top:56px;font-family:"Alfa Slab One",serif;color:#3a1606;font-size:22px;line-height:22px}
.free-label b{color:var(--white);font-weight:400;font-size:30px}
.download-icon{position:absolute;left:284px;top:14px}
.signup-title{position:absolute;left:16px;top:4px;font-family:"Arvo",serif;font-weight:700;font-size:26px;color:#111}
.signup-field{position:absolute;left:16px;top:44px;width:334px;height:28px;background:var(--white);
  border:1px solid #999;font-size:12px;color:#666;padding:6px 8px}
.signup-button{position:absolute;left:16px;top:82px;width:114px;height:28px;background:#111;
  border:1px solid #555;color:var(--white);font-family:"Arvo",serif;font-weight:700;font-size:15px;text-align:center;line-height:26px}

.site-footer{position:absolute;left:0;top:1130px;width:1188px;height:70px;
  background:linear-gradient(180deg,var(--red) 0%,var(--orange) 60%,var(--gold) 100%);
  text-align:center;font-size:12.5px;color:#111}
.footer-links{padding-top:19px}
.footer-links a{margin:0 12px}
.copyright{margin-top:4px}
</style>
</head>
<body>

<nav class="main-nav">
  <a href="#">ABOUT</a><a href="#">BOOKS</a><a href="#">VELM QUARTER</a><a href="#">BLOG</a><a href="#">CONTACT</a>
</nav>

<section class="intro-panel">
  <h2 class="intro-title">INTRODUCTION</h2>
  <div class="intro-copy">
    <p>In a secret laboratory hidden under the desert, a covert bioengineering project-codename “Exodus”-has discovered the gene responsible for the human soul.</p>
    <p>Somewhere in the neon sprawl outside the nation’s collapsing economic core, a group of renegade monks are on the verge of uncovering a secret that has eluded mankind for centuries.<br>In a glittering tower high above the urban decay, an ascendant U.S. Senator</p>
    <p>is found dead-an apparent, yet inexplicable, suicide.<br>And in the streets below, a young man races through an ultra modern metropolis on the verge of a violent revolution....closing in on the terrible truth behind Exodus-and one man’s dark vision for the future of mankind.</p>
    <p>WELCOME TO VELM QUARTER.</p>
  </div>
  <div class="intro-signature">MARCUS PELLERIN</div>
</section>

<div class="cover-art" role="img" aria-label="Book cover artwork for Harbor by Marcus Pellerin: dark futuristic city skyline with towers, helicopters, a large billboard and the cover's title and angled author-name lettering"></div>

<section class="author-words">
  <h2 class="section-title">words from the Author</h2>
  <div class="review">
    <p>Harbor is a thrill-a-minute, bio-punk myth that manages to wrestle with the most pressing issues of the new millennium. Pellerin has crafted a kickass novel of tomorrow night, when the big party gets raided by the monsters we’ve been brewing for the last half-century. Hip and hellish, wild and weird, Velm Quarter is the dystopian megalopolis</p>
    <p>into which we’re all soon moving—whether we know it or not. Toss Walter Brennick, Adrian Volk and Daniel Forsythe into the Petri dish, irradiate them, then cut the result with Transylvanian meth</p>
  </div>
  <p class="review-source">Jonah Carraway, author of <em>Crate Eleven</em> &amp; <em>The Lamplighter</em></p>
</section>

<aside class="retailers">
  <h2 class="section-title">List of Shop/Retailers</h2>
  <ul class="retail-list">
    <li>Shop Name, Place</li><li>Shop Name, Place</li><li>Shop Name, Place</li><li>Shop Name, Place</li>
    <li>Shop Name, Place</li><li>Shop Name, Place</li><li>Shop Name, Place</li>
  </ul>
</aside>
<a class="more-shops" href="#">More Shops</a>

<a class="promo promo-buy" href="#">
  <div class="buy-label">BUY<br>PAPERBACK<small>Order Online</small></div>
  <div class="book-thumb" role="img" aria-label="Small book cover thumbnail"></div>
  <div class="price-tag">$24.55</div>
</a>

<a class="promo promo-free" href="#">
  <div class="free-label"><b>FREE</b> Download<br>FIRST 4 CHAPTERS</div>
  <svg class="download-icon" width="72" height="82" viewBox="0 0 72 82" aria-hidden="true">
    <path d="M4 2h50l16 16v62H4z" fill="#fff" stroke="#ccc" stroke-width="2"/>
    <path d="M54 2v16h16" fill="#eee" stroke="#ccc" stroke-width="2"/>
    <path d="M28 18h16v24h12L36 64 16 42h12z" fill="#3fae2a" stroke="#2b7d1c" stroke-width="2"/>
  </svg>
</a>

<section class="promo promo-signup">
  <h2 class="signup-title">Email List Sign Up</h2>
  <div class="signup-field">Your email id</div>
  <div class="signup-button">SUBMIT</div>
</section>

<footer class="site-footer">
  <div class="footer-links">
    <a href="#">Home</a><span>|</span><a href="#">About</a><span>|</span><a href="#">VelmQuarter</a><span>|</span><a href="#">Blog</a><span>|</span><a href="#">Contact</a><span>|</span><a href="#">Sitemap</a><span>|</span><a href="#">Privacy Policy</a><span>|</span><a href="#">Terms &amp; Conditions</a>
  </div>
  <p class="copyright">© 2011, All Rights Reserved, Marcus Pellerin</p>
</footer>

</body>
</html>
```